Tarrow Consulting WA Business Card

Create an interesting, eye catching and colourful two sided business card. We are a business consulting operation assisting SME's improve all areas of their business. We provide consulting services to assist SME's to create a culture of continuous improvement, making a positive difference in the business. Our tag line is Small changes, big rewards. We want to create a well recognised, innovative brand that can be continued throughout our website, social media and email correspondence.

Target Market(s)

Small to Medium Enterprise Business Owners

Industry/Entity Type

Business Consultant

Contact Information for Business Card

Name of Business: Tarrow Consulting - Small Changes Big Rewards
Dean Fordyce Ph 0407358114 Moira Fordyce Ph 0407935281
Email tarrowconsultingwa@mailbox-example.com
Web address TBA
FaceBook page TBA

BACKSIDE OF CARD

Providing assistance with:

• Organisation & Efficiency
• Revenue generation & Marketing
• Financial Management
• Production quality & delivery
• Systems & Process documentation
• Exit Strategy

Font styles to use
Other font styles liked:
• Calibri

Colors

Designer to choose colors to be used in the design.

Requirements
Must have
• Calibri font

```html
<!DOCTYPE html>
<html lang="en">
<head>
<meta charset="utf-8">
<title>Tarrow Consulting WA Business Card</title>
<link rel="stylesheet" href="https://fonts.googleapis.com/css2?family=Carlito:wght@400;700&family=Arimo:wght@400&display=swap">
<style>
  :root {
    --backdrop: #4a4a4c;
    --card: #ffffff;
    --brand-red: #e8372b;
    --brand-blue: #1a6fb5;
    --ink: #222222;
    --icon-blue: #2a86c9;
  }
  * { box-sizing: border-box; margin: 0; padding: 0; }
  html, body {
    width: 1200px; height: 1000px; overflow: hidden;
    background: var(--backdrop);
  }
  .canvas { position: relative; width: 1200px; height: 1000px; }
  .card {
    position: absolute; left: 220px; width: 760px; height: 440px;
    background: var(--card); border-radius: 28px;
    font-family: "Carlito", Calibri, sans-serif;
  }
  .card--front { top: 40px; }
  .card--contact { top: 520px; }

  /* Front */
  .brand-mark {
    position: absolute; left: 0; right: 0; top: 150px;
    display: flex; justify-content: center; align-items: center; gap: 14px;
  }
  .brand-mark__dot { width: 26px; height: 26px; border-radius: 50%; background: var(--brand-red); }
  .brand-mark__name {
    font-weight: 700; font-size: 40px; color: var(--brand-red); letter-spacing: 1px;
  }
  .front-heading {
    position: absolute; left: 0; right: 0; top: 262px; text-align: center;
    font-weight: 700; font-size: 22px; color: var(--brand-blue); letter-spacing: 0.5px;
  }
  .services {
    position: absolute; left: 0; right: 0; top: 300px; text-align: center;
    font-size: 18px; line-height: 28px; color: var(--ink);
  }

  /* Contact side */
  .people { position: absolute; left: 56px; top: 70px; }
  .person { margin-bottom: 22px; }
  .person__name {
    font-weight: 700; font-size: 27px; color: var(--brand-blue); letter-spacing: 0.5px;
  }
  .person__phone {
    display: flex; align-items: center; gap: 8px;
    font-family: "Arimo", Arial, sans-serif; font-size: 24px; color: var(--ink);
  }
  .icon { width: 18px; height: 18px; flex: none; }
  .links { position: absolute; left: 56px; top: 318px; }
  .link {
    display: flex; align-items: center; gap: 10px; margin-bottom: 10px;
    font-family: "Arimo", Arial, sans-serif; font-size: 18px; color: var(--ink);
  }
  .link__dot { width: 14px; height: 14px; border-radius: 50%; background: var(--icon-blue); }
  .link--web { position: absolute; left: 410px; top: 372px; margin: 0; }
  .brand-lockup {
    position: absolute; right: 50px; top: 210px; text-align: center;
  }
  .brand-lockup .brand-mark__name { font-size: 34px; }
  .brand-lockup__row { display: flex; align-items: center; gap: 12px; justify-content: center; }
  .brand-lockup .brand-mark__dot { width: 22px; height: 22px; }
  .tagline {
    margin-top: 4px; font-size: 17px; color: var(--ink); letter-spacing: 0.5px;
  }
</style>
</head>
<body>
<div class="canvas">

  <section class="card card--front">
    <div class="brand-mark">
      <span class="brand-mark__dot"></span>
      <span class="brand-mark__name">TARROW CONSULTING</span>
    </div>
    <p class="front-heading">CREATING A CULTURE OF CONTINUOUS IMPROVEMENT</p>
    <p class="services">
      Organisation &amp; Efficiency | Revenue generation &amp; Marketing | Financial Management<br>
      Production quality &amp; delivery | Systems &amp; Process documentation | Exit Strategy
    </p>
  </section>

  <section class="card card--contact">
    <div class="people">
      <div class="person">
        <p class="person__name">DEAN FORDYCE</p>
        <p class="person__phone">
          <svg class="icon" viewBox="0 0 24 24"><path fill="var(--icon-blue)" d="M6.6 10.8a15.2 15.2 0 0 0 6.6 6.6l2.2-2.2c.3-.3.7-.4 1-.2 1.1.4 2.3.6 3.6.6.6 0 1 .4 1 1V20c0 .6-.4 1-1 1A17 17 0 0 1 3 4c0-.6.4-1 1-1h3.5c.6 0 1 .4 1 1 0 1.3.2 2.5.6 3.6.1.3 0 .7-.2 1z"/></svg>
          0407358114
        </p>
      </div>
      <div class="person">
        <p class="person__name">MOIRA FORDYCE</p>
        <p class="person__phone">
          <svg class="icon" viewBox="0 0 24 24"><path fill="var(--icon-blue)" d="M6.6 10.8a15.2 15.2 0 0 0 6.6 6.6l2.2-2.2c.3-.3.7-.4 1-.2 1.1.4 2.3.6 3.6.6.6 0 1 .4 1 1V20c0 .6-.4 1-1 1A17 17 0 0 1 3 4c0-.6.4-1 1-1h3.5c.6 0 1 .4 1 1 0 1.3.2 2.5.6 3.6.1.3 0 .7-.2 1z"/></svg>
          0407935281
        </p>
      </div>
    </div>

    <div class="links">
      <p class="link">
        <svg class="icon" viewBox="0 0 24 24"><rect x="2" y="5" width="20" height="14" rx="2" fill="none" stroke="var(--icon-blue)" stroke-width="2"/><path d="M3 6l9 7 9-7" fill="none" stroke="var(--icon-blue)" stroke-width="2"/></svg>
        tarrowconsultingwa@mailbox-example.com
      </p>
      <p class="link">
        <span class="link__dot"></span>
        tarrowconsult
      </p>
    </div>

    <p class="link link--web">
      <svg class="icon" viewBox="0 0 24 24"><circle cx="12" cy="12" r="9" fill="none" stroke="var(--icon-blue)" stroke-width="2"/><path d="M3 12h18M12 3c3 3 3 15 0 18M12 3c-3 3-3 15 0 18" fill="none" stroke="var(--icon-blue)" stroke-width="1.6"/></svg>
      www.tarrowconsult.example
    </p>

    <div class="brand-lockup">
      <div class="brand-lockup__row">
        <span class="brand-mark__dot"></span>
        <span class="brand-mark__name">TARROW CONSULTING</span>
      </div>
      <p class="tagline">SMALL CHANGES * BIG REWARDS</p>
    </div>
  </section>

</div>
</body>
</html>
```